Design of two graphics from basic existing design & colours

I have two graphics which I currently use but they are nothing special. We would like to transform these two graphics, using our existing logo colour, into something special. The outputs will be used:

- on our website;
- in a powerpoint sales presentation;
- in email campaigns; and
- to print for handing to prospects at the end of a sales presentation.

Please just submit one of the graphics and if we like the design, we will ask you to work on the second graphic. These two graphics are critical to our marketing and will be used together so we need them to have a similar look and feel.

```html
<!DOCTYPE html>
<html lang="en">
<head>
<meta charset="utf-8">
<title>Meridian Stewardship – Leadership Framework</title>
<link href="https://fonts.googleapis.com/css2?family=PT+Sans:wght@400;700&display=swap" rel="stylesheet">
<style>
  :root {
    --bg: #ffffff;
    --face-light: #d3121a;
    --face-mid: #9e0d12;
    --face-dark: #5a0808;
    --back-dark: #4a0606;
    --back-mid: #6e0b0c;
    --text-light: #ffffff;
    --culture-title: #c4121a;
    --culture-text: #6a0e10;
    --culture-accent: #c4121a;
    --hub-light: #ffffff;
    --hub-grey: #a9a9a9;
    --brand: #7a0d0f;
  }
  * { margin: 0; padding: 0; box-sizing: border-box; }
  html, body { width: 1200px; height: 848px; overflow: hidden; background: var(--bg); }
  .framework {
    position: relative;
    width: 1200px;
    height: 848px;
    font-family: "PT Sans", sans-serif;
    font-weight: 700;
  }
  .framework__shapes { position: absolute; inset: 0; }
  .pillar__stack { filter: drop-shadow(6px 8px 8px rgba(0,0,0,0.45)); }
  .pillar__title {
    position: absolute;
    color: var(--text-light);
    font-size: 26px;
    line-height: 1;
    text-align: center;
    transform: translateX(-50%);
    white-space: nowrap;
  }
  .pillar__list {
    position: absolute;
    list-style: none;
    color: var(--text-light);
    font-size: 16px;
    line-height: 26px;
  }
  .pillar__list li::before { content: "•"; margin-right: 6px; }
  .culture__title {
    position: absolute;
    left: 600px; top: 420px;
    transform: translateX(-50%);
    color: var(--culture-title);
    font-size: 26px;
  }
  .culture__list {
    position: absolute;
    list-style: none;
    color: var(--culture-text);
    font-size: 16px;
    line-height: 25.6px;
  }
  .culture__list li::before { content: "•"; margin-right: 6px; }
  .culture__list .is-accent { color: var(--culture-accent); }
  .brand {
    position: absolute;
    left: 915px; top: 60px;
    width: 260px;
    text-align: center;
    color: var(--brand);
    font-family: "PT Sans", sans-serif;
    font-weight: 700;
  }
  .brand__dot {
    width: 110px; height: 110px;
    border-radius: 50%;
    background: var(--brand);
    margin: 0 auto 22px;
  }
  .brand__name { font-size: 40px; line-height: 1.05; letter-spacing: 1px; }
  .brand__sub { font-size: 22px; letter-spacing: 3px; }
</style>
</head>
<body>
<main class="framework">
  <svg class="framework__shapes" width="1200" height="848" viewBox="0 0 1200 848" aria-hidden="true">
    <defs>
      <radialGradient id="face" cx="50%" cy="45%" r="65%">
        <stop offset="0%" stop-color="var(--face-light)"/>
        <stop offset="55%" stop-color="var(--face-mid)"/>
        <stop offset="100%" stop-color="var(--face-dark)"/>
      </radialGradient>
      <linearGradient id="back" x1="0" y1="0" x2="1" y2="1">
        <stop offset="0%" stop-color="var(--back-mid)"/>
        <stop offset="100%" stop-color="var(--back-dark)"/>
      </linearGradient>
      <radialGradient id="hub" cx="50%" cy="78%" r="70%">
        <stop offset="0%" stop-color="var(--hub-light)"/>
        <stop offset="45%" stop-color="#e6e6e6"/>
        <stop offset="100%" stop-color="var(--hub-grey)"/>
      </radialGradient>
      <g id="stack" class="pillar__stack">
        <rect x="-132" y="-132" width="264" height="264" fill="url(#back)" transform="rotate(38)"/>
        <rect x="-132" y="-132" width="264" height="264" fill="url(#back)" transform="rotate(18)"/>
        <rect x="-132" y="-132" width="264" height="264" fill="url(#face)" transform="rotate(-8)"/>
      </g>
    </defs>

    <polygon class="culture__hub" points="593,215 190,665 1011,665" fill="url(#hub)"/>

    <use href="#stack" transform="translate(593,178)"/>
    <use href="#stack" transform="translate(190,632)"/>
    <use href="#stack" transform="translate(1011,636)"/>
  </svg>

  <section class="pillar pillar--strategic">
    <h2 class="pillar__title" style="left:593px; top:104px;">Strategic</h2>
    <ul class="pillar__list" style="left:496px; top:174px;">
      <li>Board</li><li>Purpose</li><li>Risk</li><li>Strategy</li>
    </ul>
    <ul class="pillar__list" style="left:621px; top:174px;">
      <li>Structure</li><li>Values</li><li>Vision</li>
    </ul>
  </section>

  <section class="pillar pillar--financial">
    <h2 class="pillar__title" style="left:187px; top:544px;">Financial</h2>
    <ul class="pillar__list" style="left:82px; top:599px;">
      <li>Budget</li><li>CAPEX</li><li>Cash flow</li>
    </ul>
    <ul class="pillar__list" style="left:206px; top:599px;">
      <li>Delegations</li><li>OPEX</li>
    </ul>
  </section>

  <section class="pillar pillar--operational">
    <h2 class="pillar__title" style="left:1008px; top:544px;">Operational</h2>
    <ul class="pillar__list" style="left:902px; top:599px;">
      <li>Competitor</li><li>Compliance</li><li>Customer</li><li>Marketing</li><li>Meetings</li>
    </ul>
    <ul class="pillar__list" style="left:1028px; top:599px;">
      <li>Planning</li><li>Policy</li><li>Projects</li><li>Reporting</li><li>Review</li>
    </ul>
  </section>

  <section class="culture">
    <h2 class="culture__title">Cultural</h2>
    <ul class="culture__list" style="left:450px; top:465px;">
      <li>Coaching</li><li>Communication</li><li class="is-accent">Competencies</li><li>Development</li><li>Employment</li>
    </ul>
    <ul class="culture__list" style="left:622px; top:465px;">
      <li>Leadership</li><li class="is-accent">Performance</li><li>Profiles</li><li>Succession</li><li>Teams</li>
    </ul>
  </section>

  <div class="brand">
    <div class="brand__dot"></div>
    <div class="brand__name">MERIDIAN</div>
    <div class="brand__sub">STEWARDSHIP</div>
  </div>
</main>
</body>
</html>
```